依頼詳細
高速ジェット船を利用して婚活という事がわかるよう記載
ふたりの約束地めぐり記載
女性は梅原埠頭から乗船、男性は館山市在住を対象
到着後館山市内(ふたりの約束地めぐり)を観光
女性が乗船する高速船
往路竹芝7:50 館山9:25 復路 館山16:10竹芝17:25
内容
しおさい広場(お見合い回転ずし・シーグラス等を使った物作り体験)→岬原灯台(車窓)→海鮮の昼食→青葉丘城→北浜桟橋(フリータイム)
※ふたりの約束地 ・北浜桟橋・岬原灯台・青葉丘城
参加費
女性 ¥6,000男性 ¥8,000
画像が必要な場合は以下より使用が可能です。
https://pics.nuvolashare.example/album/Zq83kLmWp2TrXv9BnQe7?key=Hs4Ld8Rk2Mw6Py1Ct5
必ずこちらの画像を使わなければならないというわけではありません。
館山=海・花・海鮮です。
女性受けしそうなチラシをお願いします。

館山市役所HP
http://www.town.midorikawa.example.jp/index.html
海汽船HP
http://www.seiyokaiun.example.jp/

記載項目
高速ジェット船利用がわかるよう
旅行企画実施:㈱ソラノミチツーリスト(千葉県知事登録旅行業 第2種ー918)
主催:㈱ソラノミチツーリスト 館山市
後日QR添付
サイズ
A4
ページ数
両面
希望イメージ
シンプル 複雑
単色 カラフル
暗い 明るい
日常 高級
遊び心 厳粛
未来的 伝統的
女性的 男性的
希望する色
納品ファイル
• イラストレーター形式 (.ai)
• PNG形式 (.png)
補足説明
締め切り期間を延長させて頂きます。
西陽海運高速ジェット船を利用する事、ふたりの約束地 鏡ケ浦から富士のみえるまち館山
がわかるようなチラシをよろしくお願い致します。
前回使用した婚活チラシを添付させていただきます。
婚活、その次に観光という形です。南房総観光バスツアー募集みたいな感じではなく
婚活をしたい方対象募集ということがわかるようにお願いいたします。
■ 選んだ理由

海と花のまち館山がうまくデザインされておりまた、今回港活性化事業も目的の一つでもあったのでさり気なく表現されていたことや当日ツアー内容がわかりやすかったため当選させて頂きました。

■ 提案者全員のお礼・コメント

皆様ご提案頂きありがとうございますした。
多くの方が館山の魅力が伝わるデザインをご提案して頂きとても感謝しています。今後も婚活ツアーや婚活パーティー等のチラシ依頼をさせて頂きます。またご縁がありましたら是非ご提案していただければ幸いです。
今回こちらのコンペに参加して頂きありがとうございました。今後ともよろしくお願い致します。

```html
<!DOCTYPE html>
<html lang="ja">
<head>
<meta charset="utf-8">
<title>高速ジェット船で行く 1日婚活観光</title>
<link rel="stylesheet" href="https://fonts.googleapis.com/css2?family=Noto+Sans+JP:wght@400;500;700;900&family=Noto+Serif+JP:wght@500;700&family=Lato:wght@700;900&family=Great+Vibes&display=swap">
<style>
  :root {
    --green-deep: #2f5e1c;
    --green-main: #5f9a2f;
    --green-light: #b9d98a;
    --green-pale: #e6f2cf;
    --white: #ffffff;
    --ink: #33421f;
    --pink: #e36a7a;
  }
  * { margin: 0; padding: 0; box-sizing: border-box; }
  html, body { overflow: hidden; }
  body { width: 849px; height: 1200px; background: var(--white); }
  .flyer {
    position: relative; width: 849px; height: 1200px; overflow: hidden;
    font-family: "Noto Sans JP", sans-serif; color: var(--white);
  }
  .backdrop {
    position: absolute; inset: 0;
    background:
      radial-gradient(circle at 20% 15%, rgba(255,255,230,.55) 0, rgba(255,255,230,0) 22%),
      radial-gradient(circle at 80% 30%, rgba(230,245,190,.5) 0, rgba(230,245,190,0) 25%),
      radial-gradient(circle at 70% 80%, rgba(200,230,150,.4) 0, rgba(200,230,150,0) 30%),
      linear-gradient(170deg, #a7cf6c 0%, #7fb445 35%, #5f9a2f 65%, #3f7422 100%);
  }
  .tag {
    position: absolute; left: -60px; top: 55px; width: 340px; height: 72px;
    background: var(--white); transform: rotate(-30deg);
    display: flex; flex-direction: column; align-items: center; justify-content: center;
    color: var(--green-deep); box-shadow: 0 2px 6px rgba(0,0,0,.15);
  }
  .tag-en { font-family: "Great Vibes", cursive; font-size: 32px; line-height: 1; color: var(--pink); }
  .tag-jp { font-size: 14px; font-weight: 700; letter-spacing: .05em; line-height: 1.3; }
  .catch {
    position: absolute; top: 200px; left: 0; width: 100%; text-align: center;
    font-family: "Noto Serif JP", serif; font-size: 26px; line-height: 1.3; letter-spacing: .12em;
    text-shadow: 0 1px 4px rgba(0,0,0,.25);
  }
  .title-band {
    position: absolute; top: 252px; left: 190px; width: 470px; height: 70px;
    background: rgba(255,255,255,.92); border-radius: 4px;
    display: flex; align-items: center; justify-content: center;
    color: var(--green-deep); font-weight: 900; font-size: 42px; letter-spacing: .02em;
  }
  .title-main {
    position: absolute; top: 335px; left: 0; width: 100%; height: 90px;
    display: flex; align-items: center; justify-content: center; gap: 14px;
    color: var(--white); font-weight: 900; font-size: 76px; line-height: 1; letter-spacing: .06em;
    text-shadow: 0 2px 6px rgba(0,0,0,.25);
  }
  .day-badge {
    width: 76px; height: 76px; border-radius: 50%; background: var(--white);
    color: var(--green-main); font-size: 44px; display: flex; align-items: center; justify-content: center;
    text-shadow: none; letter-spacing: 0;
  }
  .day-badge small { font-size: 34px; }
  .subtitle {
    position: absolute; top: 458px; left: 0; width: 100%; text-align: center;
    font-family: "Noto Serif JP", serif; font-size: 22px; line-height: 1.3; letter-spacing: .06em;
  }
  .ship-art { position: absolute; left: 540px; top: 505px; width: 309px; height: 230px; }
  .place {
    position: absolute; top: 560px; left: 0; width: 100%; text-align: center;
    font-family: "Noto Serif JP", serif; font-size: 40px; font-weight: 700; line-height: 1.3;
  }
  .place small { font-size: 28px; }
  .date {
    position: absolute; top: 655px; left: 140px; display: flex; align-items: flex-start; gap: 12px;
    font-family: "Lato", sans-serif; font-weight: 900;
  }
  .date-day { font-size: 84px; line-height: 1; }
  .date-year { font-size: 30px; line-height: 1.05; padding-top: 8px; }
  .hours {
    position: absolute; top: 748px; left: 140px; font-family: "Lato", sans-serif;
    font-weight: 900; font-size: 52px; line-height: 1;
  }
  .target {
    position: absolute; left: 560px; top: 735px; width: 190px; height: 175px;
    border-radius: 50%; background: var(--white); color: var(--ink);
    display: flex; flex-direction: column; align-items: center; justify-content: center; text-align: center;
  }
  .target-label {
    background: var(--green-main); color: var(--white); font-size: 16px; font-weight: 700;
    padding: 1px 14px; border-radius: 14px; margin-bottom: 4px; line-height: 1.5;
  }
  .target-line { font-size: 23px; font-weight: 900; line-height: 1.3; }
  .people-art { position: absolute; left: 600px; top: 915px; width: 110px; height: 80px; }
  .schedule {
    position: absolute; top: 822px; left: 140px; font-size: 25px; font-weight: 700; line-height: 1.5;
  }
  .notes { position: absolute; top: 910px; left: 140px; font-size: 13px; line-height: 1.9; }
  .fee-label {
    display: inline-block; background: var(--white); color: var(--green-deep);
    font-weight: 700; padding: 0 8px; margin-right: 8px; border-radius: 3px; line-height: 1.6;
  }
  .fee { font-weight: 700; }
  .footer {
    position: absolute; left: 140px; top: 1062px; right: 40px;
    font-size: 15px; line-height: 1.7; display: flex; flex-direction: column;
  }
</style>
</head>
<body>
<main class="flyer">
  <div class="backdrop" role="img" aria-label="館山の海と緑を思わせる、柔らかくぼけた光の写真"></div>

  <div class="tag">
    <span class="tag-en">Romantic Spot</span>
    <span class="tag-jp">ロマンチックスポットを巡る</span>
  </div>

  <p class="catch">偶然の出会いに会いに行こう</p>

  <h1>
    <span class="title-band">高速ジェット船で行く</span>
    <span class="title-main"><span class="day-badge">1<small>日</small></span>婚活観光</span>
  </h1>
  <p class="subtitle">marriage hunting one-day trip</p>

  <svg class="ship-art" role="img" aria-label="白い高速ジェット船のイラスト" viewBox="0 0 309 230">
    <rect x="0" y="0" width="309" height="230" rx="20" fill="#ffffff" opacity=".28"/>
  </svg>

  <p class="place">in 千葉<small>（館山）</small></p>

  <div class="date">
    <span class="date-day">12/12</span>
    <span class="date-year">2017<br>TUD</span>
  </div>
  <p class="hours">11:00～19:00</p>

  <div class="target">
    <span class="target-label">対象者</span>
    <span class="target-line">20～40代<br>独身男女<br>男女各15名</span>
  </div>
  <svg class="people-art" role="img" aria-label="男女を表す人型のピクトグラム" viewBox="0 0 110 80">
    <rect x="0" y="0" width="110" height="80" rx="10" fill="#e6f2cf" opacity=".5"/>
  </svg>

  <div class="schedule">
    往路／梅原 7:50・館山 9:25<br>
    復路／館山16:10・梅原17:25
  </div>

  <div class="notes">
    女性は「梅原埠頭」から乗船、男性は「館山市在住」を対象<br>
    <span class="fee-label">参加費</span><span class="fee">女性 ¥6,000(税込)／男性 ¥8,000(税込)</span>
  </div>

  <footer class="footer">
    <span>旅行企画実施：(株)ソラノミチツーリスト（千葉県知事登録旅行業 第2種ー918）</span>
    <span>主催：(株)ソラノミチツーリスト 館山市</span>
  </footer>
</main>
</body>
</html>
```